Open Now Poster for Retail Shop windows.

To design a poster to be printed to put on the windows of our retail stores to tell customers that we are open. Size is to be 590mm W x 840mm H supplied as a pdf. Design should incorporate our logo as well as other elements which indicate the style of our shop which is Womens Beach, Resort & Casual Clothing, Swimwear and Accessories. I would like the design to incorporate the words "Open Now" in some form in large lettering. I would also like the poster to be timeless and able to be used for other wording, so no images would be preferable.

Target Market(s)

Womens Beach, Resort & Casual Clothing, Swimwear and Accessories

Industry/Entity Type

Retail

Colors
e34297

Requirements
Must have
• words "Open Now". as well as our logo.

```html
<!DOCTYPE html>
<html lang="en">
<head>
<meta charset="utf-8">
<title>Now Open – Window Poster</title>
<link href="https://fonts.googleapis.com/css2?family=Damion&display=swap" rel="stylesheet">
<style>
  :root {
    --pink-deep: #8c0f55;
    --pink-core: #e6058f;
    --pink-brand: #e34297;
    --pink-soft: #f27cbc;
    --blush: #f7d4e6;
    --shadow-plum: #6b0a3e;
    --white: #ffffff;
  }
  html, body {
    margin: 0;
    padding: 0;
    width: 843px;
    height: 1200px;
    overflow: hidden;
    background: var(--white);
  }
  .poster {
    position: relative;
    width: 843px;
    height: 1200px;
    overflow: hidden;
    background:
      radial-gradient(ellipse at 70% 38%, var(--pink-core) 0%, #d7067f 45%, var(--pink-deep) 100%);
  }
  .poster__glow {
    position: absolute;
    inset: 0;
  }
  .poster__headline {
    position: absolute;
    margin: 0;
    font-family: "Damion", cursive;
    font-weight: 400;
    color: var(--white);
    line-height: 1;
    text-shadow: 6px 7px 0 var(--shadow-plum);
    transform-origin: left bottom;
    white-space: nowrap;
  }
  .poster__headline--now {
    left: 205px;
    top: 165px;
    font-size: 300px;
    transform: rotate(-12deg);
  }
  .poster__headline--open {
    left: 55px;
    top: 420px;
    font-size: 385px;
    transform: rotate(-12deg);
  }
  .brand {
    position: absolute;
    left: 24px;
    bottom: 30px;
    margin: 0;
    font-family: "Damion", cursive;
    font-size: 84px;
    line-height: 1;
    color: var(--pink-core);
  }
</style>
</head>
<body>
  <main class="poster">
    <svg class="poster__glow" width="843" height="1200" viewBox="0 0 843 1200"
         role="img" aria-label="Soft abstract background of pink light rays, glowing bokeh circles and flowing white waves">
      <defs>
        <linearGradient id="wave-fade" x1="0" y1="0" x2="1" y2="1">
          <stop offset="0" stop-color="#ffffff" stop-opacity="0.85"/>
          <stop offset="1" stop-color="#f7d4e6" stop-opacity="0.2"/>
        </linearGradient>
        <radialGradient id="lower-haze" cx="0.2" cy="0.9" r="0.8">
          <stop offset="0" stop-color="#f7d4e6" stop-opacity="0.9"/>
          <stop offset="1" stop-color="#f27cbc" stop-opacity="0"/>
        </radialGradient>
      </defs>
      <g fill="#ffffff" opacity="0.12">
        <circle cx="440" cy="700" r="90"/>
        <circle cx="570" cy="680" r="28"/>
        <circle cx="680" cy="800" r="70"/>
        <circle cx="370" cy="860" r="85"/>
        <circle cx="480" cy="930" r="70"/>
        <circle cx="150" cy="760" r="45"/>
      </g>
      <rect x="0" y="650" width="843" height="550" fill="url(#lower-haze)"/>
      <path d="M0 780 C 200 860, 330 1000, 520 1080 S 780 1120, 843 1100 L 843 1200 L 0 1200 Z"
            fill="url(#wave-fade)" opacity="0.55"/>
      <path d="M0 900 C 180 960, 330 1080, 560 1090 S 800 1010, 843 1000"
            fill="none" stroke="#ffffff" stroke-opacity="0.6" stroke-width="10"/>
      <path d="M300 1200 C 450 1100, 650 1050, 843 1040 L 843 1200 Z"
            fill="#8c0f55" opacity="0.8"/>
    </svg>

    <h1 class="poster__headline poster__headline--now">Now</h1>
    <p class="poster__headline poster__headline--open">Open</p>

    <p class="brand">tidelle</p>
  </main>
</body>
</html>
```